Flyer for the Lumen 2025 Conference

I am looking to produce a flyer for our upcoming conference, Lumen 2025. This is an annual conference that we plan to publicize on social media. The ideal designer will create a flyer that is eye-catching and effectively communicates the key information. Please see attached our logo, speaker photo, and flyer content.

Target Market(s)

All demographics

Industry/Entity Type

Christian

Font styles to use
Sans Serif

Requirements
Should not have
• Cross, church

```html
<!DOCTYPE html>
<html lang="en">
<head>
<meta charset="utf-8">
<title>Lumen 2025 Conference Flyer</title>
<link href="https://fonts.googleapis.com/css2?family=Jost:wght@400;500;600;700&display=swap" rel="stylesheet">
<style>
  :root{
    --sky-light:#9fd0f5;
    --sky-mid:#2f6fc4;
    --deep:#0c2a6b;
    --night:#07132f;
    --brand-box:#1d3c7e;
    --accent:#f47a20;
    --white:#ffffff;
  }
  *{margin:0;padding:0;box-sizing:border-box;}
  html,body{width:848px;height:1200px;overflow:hidden;background:var(--night);}
  body{font-family:"Jost",sans-serif;color:var(--white);}
  .flyer{position:relative;width:848px;height:1200px;overflow:hidden;}
  .backdrop{
    position:absolute;inset:0;
    background:
      radial-gradient(ellipse 260px 220px at 420px 150px, rgba(235,246,255,.95), rgba(160,210,250,.5) 45%, rgba(0,0,0,0) 100%),
      linear-gradient(180deg, var(--sky-light) 0%, var(--sky-mid) 18%, #1c4ea5 32%, var(--deep) 55%, var(--night) 100%);
  }
  .speaker-photo{
    position:absolute;left:226px;top:282px;width:622px;height:918px;
    border-radius:300px 300px 0 0;
    background:
      radial-gradient(ellipse 120px 150px at 370px 140px, rgba(110,70,45,.55), rgba(0,0,0,0) 100%),
      linear-gradient(180deg, rgba(30,90,200,.35) 0%, rgba(25,85,200,.6) 45%, rgba(15,45,120,.6) 100%);
  }
  .brand{
    position:absolute;left:344px;top:32px;width:160px;height:160px;
    background:var(--brand-box);
    display:flex;align-items:center;justify-content:center;
    font-size:34px;font-weight:500;letter-spacing:1px;color:var(--white);
  }
  .event-name{position:absolute;left:52px;top:222px;color:var(--accent);font-size:25px;font-weight:500;line-height:31px;}
  .headline{position:absolute;left:52px;top:294px;font-size:70px;font-weight:700;line-height:63px;letter-spacing:1px;}
  .speaker-title{position:absolute;left:52px;top:530px;font-size:26px;font-weight:400;}
  .speaker-name{position:absolute;left:52px;top:566px;font-size:46px;font-weight:700;color:var(--accent);letter-spacing:.5px;}
  .venue{position:absolute;left:282px;top:741px;text-align:left;}
  .venue-small{font-size:18px;font-weight:400;letter-spacing:.3px;display:block;line-height:20px;}
  .venue-big{font-size:44px;font-weight:700;display:block;line-height:42px;letter-spacing:.5px;}
  .address{position:absolute;left:279px;top:853px;display:flex;gap:12px;align-items:center;}
  .address p{font-size:20px;line-height:24px;letter-spacing:.5px;}
  .schedule{position:absolute;left:179px;top:941px;display:flex;gap:14px;}
  .schedule ul{list-style:none;font-size:20px;line-height:24px;}
  .schedule b{font-weight:700;}
  .app-row{position:absolute;left:120px;top:1052px;display:flex;align-items:center;}
  .app-text{font-size:19px;line-height:23px;text-align:right;width:320px;}
  .app-text b{font-weight:700;}
  .badge{width:106px;height:32px;background:var(--white);border-radius:3px;margin-left:8px;}
  .contact{position:absolute;top:1141px;left:0;width:848px;display:flex;font-size:20px;font-weight:600;}
  .contact-item{position:absolute;display:flex;align-items:center;gap:8px;}
</style>
</head>
<body>
<main class="flyer">
  <div class="backdrop" role="img" aria-label="Sky of light rays shining over a calm blue sea"></div>
  <div class="speaker-photo" role="img" aria-label="Portrait of the speaker in a blue suit jacket and knit turtleneck"></div>

  <div class="brand">KAVOR</div>

  <p class="event-name">LUMEN 2025.<br>A Prophetic Conference</p>
  <h1 class="headline">THE VOICE<br>OF THE LORD</h1>

  <p class="speaker-title">Prophet</p>
  <p class="speaker-name">MARCUS OBEL</p>

  <div class="venue">
    <span class="venue-small">THE RIVERSIDE PERFORMING</span>
    <span class="venue-big">ARTS CENTER</span>
  </div>

  <div class="address">
    <svg width="42" height="50" viewBox="0 0 42 50" aria-hidden="true">
      <path d="M21 47 C21 47 4 29 4 19 A17 17 0 0 1 38 19 C38 29 21 47 21 47Z" fill="none" stroke="var(--accent)" stroke-width="4"/>
      <circle cx="21" cy="19" r="6" fill="none" stroke="var(--accent)" stroke-width="4"/>
    </svg>
    <p>238 Alder Lane<br>Brookfield, Maine 04110</p>
  </div>

  <div class="schedule">
    <svg width="48" height="44" viewBox="0 0 48 44" aria-hidden="true">
      <rect x="3" y="6" width="42" height="35" rx="3" fill="none" stroke="var(--accent)" stroke-width="4"/>
      <line x1="3" y1="14" x2="45" y2="14" stroke="var(--accent)" stroke-width="4"/>
      <g stroke="var(--accent)" stroke-width="3"><line x1="12" y1="1" x2="12" y2="10"/><line x1="20" y1="1" x2="20" y2="10"/><line x1="28" y1="1" x2="28" y2="10"/><line x1="36" y1="1" x2="36" y2="10"/></g>
      <g fill="var(--accent)"><circle cx="15" cy="28" r="2.5"/><circle cx="24" cy="28" r="2.5"/><circle cx="33" cy="28" r="2.5"/></g>
    </svg>
    <ul>
      <li>Friday, December 26th, <b>6:30PM - 9:00PM</b></li>
      <li>Saturday, December 27th, <b>5:30PM&nbsp; - 8:00PM</b></li>
      <li>Sunday, December 29th, <b>4:30PM - 7:00PM</b></li>
    </ul>
  </div>

  <div class="app-row">
    <p class="app-text">Download the <b>KAVOR</b> App to stay<br>updated on the event</p>
    <svg width="36" height="40" viewBox="0 0 36 40" style="margin-left:14px" aria-hidden="true">
      <path d="M6 4 C-2 14 16 14 10 6 C6 2 2 14 10 22 C16 28 24 30 30 30" fill="none" stroke="var(--accent)" stroke-width="2.5" stroke-linecap="round"/>
      <path d="M24 24 L31 30 L24 35" fill="none" stroke="var(--accent)" stroke-width="2.5" stroke-linecap="round" stroke-linejoin="round"/>
    </svg>
    <div class="badge" aria-label="App download badge"></div>
    <div class="badge" aria-label="App download badge"></div>
  </div>

  <div class="contact">
    <div class="contact-item" style="left:123px">
      <svg width="22" height="22" viewBox="0 0 24 24" aria-hidden="true"><path d="M5 2 L9 2 L11 7 L8.5 9 C10 12 12 14 15 15.5 L17 13 L22 15 L22 19 C22 21 20 22 18 22 C9 21 3 15 2 6 C2 4 3 2 5 2Z" fill="none" stroke="var(--accent)" stroke-width="2" stroke-linejoin="round"/></svg>
      <span>207 555 0143</span>
    </div>
    <div class="contact-item" style="left:315px">
      <svg width="22" height="22" viewBox="0 0 24 24" aria-hidden="true"><circle cx="12" cy="12" r="4" fill="none" stroke="var(--accent)" stroke-width="2"/><path d="M16 8 V14 C16 17 21 17 21 12 A9 9 0 1 0 17 19.5" fill="none" stroke="var(--accent)" stroke-width="2" stroke-linecap="round"/></svg>
      <span>hello@kavor.org</span>
    </div>
    <div class="contact-item" style="left:546px">
      <svg width="22" height="22" viewBox="0 0 24 24" aria-hidden="true"><g fill="none" stroke="var(--accent)" stroke-width="2"><circle cx="12" cy="12" r="10"/><ellipse cx="12" cy="12" rx="4.5" ry="10"/><line x1="2" y1="12" x2="22" y2="12"/><path d="M4 7 H20 M4 17 H20"/></g></svg>
      <span>www.kavor.org</span>
    </div>
  </div>
</main>
</body>
</html>
```